Visual design for database driven web application

Need a clean, professional looking visual design for a web application.

PLUMB is the new standardized K-12 school testing program for the state of Texas. We are building an application named PLUMB-Finder (clever, yeah?) that will allow teachers, school administrators, and others to EASILY sort through millions of records of student data and print or export reports showing just the information they need about their students.

The state currently doesn't provide a user-friendly way to do this. They provide a "data dump" spreadsheet that school administrators and teachers must figure out how to manipulate to get the data they need. We are building a Web-based tool that will make it super simple and easy for our users to get the data they need in a format that works for them.

I've created a basic wireframe of the main application screen in Wirella Kit Plus. I need you to "skin" the wireframe to make it look good. Your mockup will set the tone for branding and visual design throughout the site.

See the attached screenshots. There are a few variations of the screen that include dynamic panels that open & close. Start by designing just the main screen and if you have time, do one or two of the panels. Thanks!
Updates

Target Market(s)

K-12 education professionals (teachers, administrators) in the state of Texas

Industry/Entity Type

Building

Requirements
Must have
• Your mockups should include all of the features & content shown in the attached screenshots.

However, you don't have to show all 10 rows of data. You can just do the column headers and one row of data. (It would be repetitive and unnecessary to spend time re-creating the entire grid with all of that data just to show your visual styling.)

The design should reflect the following concepts:

- Texas
- Education
- Simplicity
- Helpfulness
- Trust
- Professionalism

If I select your design, I will want your design source files (Illustrator, Photoshop, etc.)
Nice to have
• A logo in the upper left corner for PLUMB-Finder. The logo should definitely communicate the design concepts described under "must have."

```html
<!DOCTYPE html>
<html lang="en">
<head>
<meta charset="utf-8">
<title>PLUMB-Finder · Students Data</title>
<link href="https://fonts.googleapis.com/css2?family=Open+Sans:wght@400;600;700&family=Arimo&display=swap" rel="stylesheet">
<style>
:root{
  --slate:#4a5e68;
  --slate-dark:#3d4f58;
  --sand:#d4d0bc;
  --page:#efefef;
  --white:#ffffff;
  --ink:#333333;
  --muted:#666666;
  --rule:#c9c9c9;
  --accent:#e0201e;
  --row-alt:#e6e6e6;
  --row:#f6f6f6;
  --btn:#8c8c8c;
}
*{box-sizing:border-box;margin:0;padding:0}
html,body{width:1097px;height:1200px;overflow:hidden;background:var(--page)}
body{font-family:"Open Sans",sans-serif;color:var(--ink)}
.app{position:relative;width:1280px;height:1400px;transform:scale(.857);transform-origin:0 0;background:var(--page)}
.masthead{position:absolute;left:0;top:0;width:1280px;height:396px;background:var(--white)}
.brand{position:absolute;left:28px;top:10px;font-size:34px;font-weight:700;color:var(--slate);letter-spacing:-1px}
.account{position:absolute;left:976px;top:0;width:274px;height:33px;background:#ececec;font-size:14px;padding:8px 0 0 18px;color:var(--ink)}
.account .links{font-size:13px;color:var(--muted);margin-left:22px}
.search{position:absolute;left:452px;top:75px;display:flex}
.search-input{width:294px;height:34px;border:1px solid #d6d6d6;border-right:none;background:#fff;border-radius:3px 0 0 3px}
.search-btn{width:120px;height:34px;background:linear-gradient(var(--slate),var(--slate-dark));color:#fff;font-size:16px;display:flex;align-items:center;gap:8px;padding-left:16px;border-radius:0 3px 3px 0}
.search-toggle{position:absolute;left:747px;top:115px;font-size:14px;color:var(--accent)}
.caret{display:inline-block;width:0;height:0;border-left:4px solid transparent;border-right:4px solid transparent;border-top:4px solid currentColor;vertical-align:middle;margin-left:6px}
.options{position:absolute;left:231px;top:137px;width:841px;height:174px;border:1px solid var(--rule);background:#fff;display:flex;padding:13px 0 0 10px}
.col{display:flex;flex-direction:column}
.opt{height:30px;font-size:14px;color:#555;display:flex;align-items:flex-start;gap:5px}
.cb{width:13px;height:13px;border:1px solid #aaa;background:#fff;margin-top:3px;position:relative;flex:none}
.cb.on::before,.cb.on::after{content:"";position:absolute;left:5px;top:1px;width:1.6px;height:9px;background:#222;transform:rotate(45deg)}
.cb.on::after{transform:rotate(-45deg)}
.tabs{position:absolute;top:356px;left:28px;display:flex;gap:8px}
.tab{width:205px;height:40px;font-size:20px;display:flex;align-items:center;justify-content:center;border-radius:2px 2px 0 0}
.tab.active{background:var(--slate);color:#fff}
.tab.idle{background:var(--sand);color:var(--slate)}
.band{position:absolute;left:0;top:396px;width:1280px;height:13px;background:var(--slate)}
.toolbar{position:absolute;top:419px;left:28px;width:1222px;font-size:15px;color:var(--muted);display:flex;align-items:center}
.toggle{margin-left:8px;width:120px;height:24px;background:linear-gradient(#9d9d9d,#7f7f7f);color:#fff;border-radius:3px;display:flex;align-items:center;padding-left:12px;font-size:15px}
.toggle .caret{margin:0 10px 0 0}
.filtered{margin-left:30px}
.filtered a{color:var(--accent)}
.export{margin-left:auto;font-size:15px;color:#888}
.export span{margin:0 12px;color:#ccc}
.grid{position:absolute;left:29px;top:543px;width:1222px;border-collapse:collapse;table-layout:fixed;font-family:"Arimo",sans-serif;font-size:16px;border:1px solid #bbb}
.grid th{height:34px;text-align:left;font-weight:400;background:#e4e4e4;border-left:1px solid #c8c8c8;padding-left:6px}
.grid td{height:36px;padding-left:6px;border-left:1px solid #d0d0d0}
.grid tbody tr:nth-child(odd){background:var(--row)}
.grid tbody tr:nth-child(even){background:var(--row-alt)}
.picker{position:absolute;left:28px;top:470px;width:733px;height:272px;background:#fff;border:1px solid #ddd;box-shadow:0 2px 10px rgba(0,0,0,.2)}
.picker-bulk{position:absolute;left:34px;top:12px;font-size:15px;color:var(--muted)}
.picker-bulk span{margin:0 8px}
.picker-cols{position:absolute;left:35px;top:55px;display:flex}
.picker-actions{position:absolute;right:52px;top:213px;display:flex;align-items:center;gap:12px;font-size:15px;color:var(--muted)}
.apply{width:69px;height:26px;background:linear-gradient(#b4b4b4,#999);color:#fff;border-radius:3px;display:flex;align-items:center;justify-content:center}
.pager{position:absolute;left:29px;top:972px;display:flex;align-items:center;font-family:"Arimo",sans-serif;font-size:15px;color:#555}
.pg{height:22px;min-width:25px;border:1px solid #bbb;display:flex;align-items:center;justify-content:center;padding:0 6px;margin-right:5px;background:#f7f7f7}
.pg.cur{background:var(--slate);color:#fff;border-color:var(--slate)}
.gap{width:82px;border-bottom:2px dotted #666;height:12px;margin:0 6px 0 4px}
.rows{margin-left:40px;display:flex;align-items:center;gap:8px;font-family:"Open Sans",sans-serif}
</style>
</head>
<body>
<div class="app">
  <header class="masthead">
    <div class="brand">PLUMB-Finder</div>
    <div class="account">Welcome, Dana <span class="links">my profile &nbsp;|&nbsp; log out</span></div>
    <div class="search">
      <div class="search-input"></div>
      <div class="search-btn"><svg width="20" height="18" viewBox="0 0 20 18"><circle cx="7" cy="7" r="5.5" fill="none" stroke="#fff" stroke-width="2"/><path d="M11 11l6 6" stroke="#fff" stroke-width="3"/></svg>Search</div>
    </div>
    <div class="search-toggle">search options<span class="caret" style="color:#555"></span></div>
    <div class="options">
      <div class="col" style="width:138px"><div class="opt"><i class="cb on"></i>Date</div><div class="opt"><i class="cb on"></i>Grade</div><div class="opt"><i class="cb"></i>ESC</div><div class="opt"><i class="cb"></i>CDCD#</div><div class="opt"><i class="cb on"></i>District</div></div>
      <div class="col" style="width:123px"><div class="opt"><i class="cb on"></i>Date</div><div class="opt"><i class="cb on"></i>Grade</div><div class="opt"><i class="cb"></i>ESC</div><div class="opt"><i class="cb"></i>CDCD#</div><div class="opt"><i class="cb on"></i>District</div></div>
      <div class="col" style="width:111px"><div class="opt"><i class="cb on"></i>Date</div><div class="opt"><i class="cb on"></i>Grade</div><div class="opt"><i class="cb"></i>ESC</div><div class="opt"><i class="cb"></i>CDCD#</div><div class="opt"><i class="cb on"></i>District</div></div>
      <div class="col" style="width:121px"><div class="opt"><i class="cb on"></i>Date</div><div class="opt"><i class="cb on"></i>Grade</div><div class="opt"><i class="cb"></i>ESC</div><div class="opt"><i class="cb"></i>CDCD#</div><div class="opt"><i class="cb on"></i>District</div></div>
      <div class="col" style="width:124px"><div class="opt"><i class="cb on"></i>Date</div><div class="opt"><i class="cb on"></i>Grade</div><div class="opt"><i class="cb"></i>ESC</div><div class="opt"><i class="cb"></i>CDCD#</div><div class="opt"><i class="cb on"></i>District</div></div>
      <div class="col" style="width:129px"><div class="opt"><i class="cb on"></i>Date</div><div class="opt"><i class="cb on"></i>Grade</div><div class="opt"><i class="cb"></i>ESC</div><div class="opt"><i class="cb"></i>CDCD#</div><div class="opt"><i class="cb on"></i>District</div></div>
      <div class="col"><div class="opt"><i class="cb on"></i>Date</div><div class="opt"><i class="cb on"></i>Grade</div><div class="opt"><i class="cb"></i>ESC</div><div class="opt"><i class="cb"></i>CDCD#</div><div class="opt"><i class="cb on"></i>District</div></div>
    </div>
    <nav class="tabs"><div class="tab active">Instructions</div><div class="tab idle">Students Data</div></nav>
  </header>
  <div class="band"></div>

  <div class="toolbar">
    Showing 26 of 38 columns
    <div class="toggle"><span class="caret"></span>Show / Hide</div>
    <div class="filtered">3 columns are <a>filtered</a></div>
    <div class="export">⎙ print<span>|</span>⤓ download</div>
  </div>

  <table class="grid">
    <colgroup><col style="width:94px"><col style="width:73px"><col style="width:79px"><col style="width:114px"><col style="width:107px"><col style="width:128px"><col style="width:131px"><col style="width:130px"><col style="width:63px"><col style="width:100px"><col style="width:97px"><col style="width:106px"></colgroup>
    <thead><tr><th>District</th><th>Grade</th><th>Age</th><th>CDCD#</th><th>Campus</th><th>Teacher</th><th>Last Name</th><th>First Name</th><th>MI</th><th>Student ID</th><th>Gender</th><th>DOB</th></tr></thead>
    <tbody>
      <tr><td>411</td><td>9</td><td>10</td><td>99990011#</td><td>EXAMPLE</td><td>EXAMPLE</td><td>EXAMPLE</td><td>EXAMPLE</td><td>10</td><td>10</td><td>MALE</td><td>10</td></tr>
      <tr><td>411</td><td>9</td><td>10</td><td>99990011#</td><td>EXAMPLE</td><td>EXAMPLE</td><td>EXAMPLE</td><td>EXAMPLE</td><td>10</td><td>10</td><td>MALE</td><td>10</td></tr>
      <tr><td>411</td><td>9</td><td>10</td><td>99990011#</td><td>EXAMPLE</td><td>EXAMPLE</td><td>EXAMPLE</td><td>EXAMPLE</td><td>10</td><td>10</td><td>MALE</td><td>10</td></tr>
      <tr><td>411</td><td>9</td><td>10</td><td>99990011#</td><td>EXAMPLE</td><td>EXAMPLE</td><td>EXAMPLE</td><td>EXAMPLE</td><td>10</td><td>10</td><td>MALE</td><td>10</td></tr>
      <tr><td>411</td><td>9</td><td>10</td><td>99990011#</td><td>EXAMPLE</td><td>EXAMPLE</td><td>EXAMPLE</td><td>EXAMPLE</td><td>10</td><td>10</td><td>MALE</td><td>10</td></tr>
      <tr><td>411</td><td>9</td><td>10</td><td>99990011#</td><td>EXAMPLE</td><td>EXAMPLE</td><td>EXAMPLE</td><td>EXAMPLE</td><td>10</td><td>10</td><td>MALE</td><td>10</td></tr>
      <tr><td>411</td><td>9</td><td>10</td><td>99990011#</td><td>EXAMPLE</td><td>EXAMPLE</td><td>EXAMPLE</td><td>EXAMPLE</td><td>10</td><td>10</td><td>MALE</td><td>10</td></tr>
      <tr><td>411</td><td>9</td><td>10</td><td>99990011#</td><td>EXAMPLE</td><td>EXAMPLE</td><td>EXAMPLE</td><td>EXAMPLE</td><td>10</td><td>10</td><td>MALE</td><td>10</td></tr>
      <tr><td>411</td><td>9</td><td>10</td><td>99990011#</td><td>EXAMPLE</td><td>EXAMPLE</td><td>EXAMPLE</td><td>EXAMPLE</td><td>10</td><td>10</td><td>MALE</td><td>10</td></tr>
      <tr><td>411</td><td>9</td><td>10</td><td>99990011#</td><td>EXAMPLE</td><td>EXAMPLE</td><td>EXAMPLE</td><td>EXAMPLE</td><td>10</td><td>10</td><td>MALE</td><td>10</td></tr>
    </tbody>
  </table>

  <div class="picker">
    <div class="picker-bulk">Check all<span>|</span>Uncheck all</div>
    <div class="picker-cols">
      <div class="col" style="width:95px"><div class="opt"><i class="cb on"></i>Date</div><div class="opt"><i class="cb on"></i>Grade</div><div class="opt"><i class="cb"></i>ESC</div><div class="opt"><i class="cb"></i>CDCD#</div><div class="opt"><i class="cb on"></i>District</div></div>
      <div class="col" style="width:93px"><div class="opt"><i class="cb on"></i>Date</div><div class="opt"><i class="cb on"></i>Grade</div><div class="opt"><i class="cb"></i>ESC</div><div class="opt"><i class="cb"></i>CDCD#</div><div class="opt"><i class="cb on"></i>District</div></div>
      <div class="col" style="width:90px"><div class="opt"><i class="cb on"></i>Date</div><div class="opt"><i class="cb on"></i>Grade</div><div class="opt"><i class="cb"></i>ESC</div><div class="opt"><i class="cb"></i>CDCD#</div><div class="opt"><i class="cb on"></i>District</div></div>
      <div class="col" style="width:92px"><div class="opt"><i class="cb on"></i>Date</div><div class="opt"><i class="cb on"></i>Grade</div><div class="opt"><i class="cb"></i>ESC</div><div class="opt"><i class="cb"></i>CDCD#</div><div class="opt"><i class="cb on"></i>District</div></div>
      <div class="col" style="width:103px"><div class="opt"><i class="cb on"></i>Date</div><div class="opt"><i class="cb on"></i>Grade</div><div class="opt"><i class="cb"></i>ESC</div><div class="opt"><i class="cb"></i>CDCD#</div><div class="opt"><i class="cb on"></i>District</div></div>
      <div class="col" style="width:102px"><div class="opt"><i class="cb on"></i>Date</div><div class="opt"><i class="cb on"></i>Grade</div><div class="opt"><i class="cb"></i>ESC</div><div class="opt"><i class="cb"></i>CDCD#</div><div class="opt"><i class="cb on"></i>District</div></div>
      <div class="col"><div class="opt"><i class="cb on"></i>Date</div><div class="opt"><i class="cb on"></i>Grade</div><div class="opt"><i class="cb"></i>ESC</div><div class="opt"><i class="cb"></i>CDCD#</div><div class="opt"><i class="cb on"></i>District</div></div>
    </div>
    <div class="picker-actions">Cancel<div class="apply">Apply</div></div>
  </div>

  <nav class="pager">
    <div class="pg">« Previous</div>
    <div style="width:14px"></div>
    <div class="pg cur">1</div><div class="pg">2</div><div class="pg">3</div><div class="pg">4</div><div class="pg">5</div>
    <div class="gap"></div>
    <div class="pg">12</div><div class="pg">13</div>
    <div class="pg" style="width:81px">Next »</div>
    <div class="rows">Show <div class="pg" style="margin:0">10<span class="caret"></span></div> rows per page</div>
  </nav>
</div>
</body>
</html>
```